Footwear & Apparel Business to Business Presentation (B2B)

We are looking for a Business to Business presentation that is simple, clean, and easy to understand.

We would like the steps to be laid out with simple graphics indicating steps 1, 2 , 3 with circles / arrows. Colours are acceptable. This is a tool to engage potential customers so needs to be very clear and easy to understand.

our logo is attached.
Updates

Target Market(s)

women aged 30 plus

Industry/Entity Type

Business

Font styles to use
Serif
Sans Serif

Requirements
Must have
• 2 pages:
• 1st page should be our logo and who we are:
• Coastal Hall Of Trends
• contact: info@chot-mail.com.au
• We are a wholesale and distribution company of footwear and apparel
• We specialize in clearing aged stock through flash sales channels in Australia and New Zealand.
• We offer suppliers an alternative inventory distribution channel.
• Take advantage of the reverse seasonality - when you can't move your winter stock, We Can!
• presentation black and white
• must look clean , simple , contemporary
• 2nd Page:
• clear detailed step by step process
• graphics demonstrating this
• suggestions:
• step by step on an pinecone flatscreen with an arrow between each step with an image on each screen and notes on the side
• we need the following 3 steps on our brief:
• 1 - we buy upfront and handle all processes
• 2 - $ in your bank
• 3 - goods shipped to Australia / New Zealand
Nice to have
• suggestions:
• -use graphics to show moving stock from north america to australia & New zealand
• -maybe a global map
• -icons showing money and transportation
• -demonstrate the 3 steps in pinecone windows
• - show the graphics / icons as a backdrop and text on top

```html
<!DOCTYPE html>
<html lang="en">
<head>
<meta charset="utf-8">
<title>Coastal Hall Of Trends – Page 1</title>
<link href="https://fonts.googleapis.com/css2?family=Arimo:wght@400;700&family=Roboto+Condensed:wght@400;500;700&display=swap" rel="stylesheet">
<style>
  :root {
    --backdrop-centre: #f6f6f6;
    --backdrop-edge: #e2e3e4;
    --sheet: #ffffff;
    --ink: #333333;
    --label-bg: #1e1e1e;
    --label-ink: #ffffff;
  }
  * { margin: 0; padding: 0; box-sizing: border-box; }
  html, body {
    width: 1200px;
    height: 1000px;
    overflow: hidden;
  }
  body {
    position: relative;
    background: radial-gradient(ellipse at 45% 45%, var(--backdrop-centre) 0%, var(--backdrop-edge) 100%);
    font-family: "Roboto Condensed", "Arial Narrow", sans-serif;
    color: var(--ink);
  }
  .sheet {
    position: absolute;
    left: 148px;
    top: 50px;
    width: 637px;
    height: 900px;
    background: var(--sheet);
  }
  .brand-name {
    position: absolute;
    left: 0;
    right: 0;
    top: 428px;
    text-align: center;
    font-family: "Roboto Condensed", "Arial Narrow", sans-serif;
    font-weight: 400;
    font-size: 14px;
    letter-spacing: 0.62em;
    padding-left: 0.62em;
    text-transform: uppercase;
    color: var(--ink);
  }
  .about {
    position: absolute;
    left: 60px;
    top: 683px;
    width: 540px;
  }
  .about-title,
  .about-contact {
    font-weight: 700;
    font-size: 16px;
    line-height: 23px;
  }
  .about-points {
    list-style: none;
    margin-top: 4px;
  }
  .about-points li {
    position: relative;
    padding-left: 20px;
    font-size: 13.5px;
    line-height: 20.5px;
  }
  .about-points li::before {
    content: "";
    position: absolute;
    left: 2px;
    top: 8px;
    width: 6px;
    height: 6px;
    border-radius: 50%;
    background: var(--ink);
  }
  .page-label {
    position: absolute;
    left: 901px;
    top: 422px;
    width: 299px;
    height: 91px;
    background: var(--label-bg);
    color: var(--label-ink);
    font-family: "Arimo", Arial, sans-serif;
    font-size: 48px;
    line-height: 86px;
    padding-left: 40px;
  }
  .page-label strong { font-weight: 700; }
</style>
</head>
<body>
  <main class="sheet">
    <div class="brand-name">Coastal Hall Of Trends</div>
    <section class="about">
      <h1 class="about-title">Coastal Hall Of Trends</h1>
      <p class="about-contact">Contact: info@chot-mail.com.au</p>
      <ul class="about-points">
        <li>Wholesale and distribution company of footwear and apparel</li>
        <li>Specialize in clearing aged stock through flash sales channels in Australia and New Zealand</li>
        <li>Offer suppliers an alternative inventory distribution channel</li>
        <li>Take advantage of the reverse seasonality</li>
        <li>when you can't move your winter stock, We Can!</li>
      </ul>
    </section>
  </main>
  <div class="page-label">Page <strong>1</strong></div>
</body>
</html>
```